Luxury Ayurvedic Hair Oil logo and package design

We need a logo and package design for our Ayurvedic and natural hair growth oil. Our company, Velmora, is the premier luxury Ayurvedic beauty brand, bringing ancient East-Indian natural and botanic health and beauty products to the US market. Our first major product - Velmora Hair Growth Oil - is a coconut oil based product that was developed by tribes in the Southern State of Kerala that includes ancient herbs like Gooseberry, Indigo, Indian Aloe, Balloon Vine and Brahmi.

The design should be catered to the high-end luxury market (minimal design, minimal text, fonts that invoke a sense of luxury). The primary colors should be deep blue for the packaging and gold for the characters (it's in the name - Velmora). We are looking to sell our products in Brenvale and Tolland Pryce and require packaging that is in line with products sold at these high-end retailers.

The final logo design and packaging should communicate luxury and the ancient wisdom of far-eastern traditions.

Target Market(s)

Velmora's main target is women who value fashionable/quality skincare, beauty, and fragrance products and are open to a medium to high price range. These women love uniqueness in brand and products that cannot be found elsewhere. They are looking for the next new "it" item that will take their haircare and beauty regiment to the next level.

Industry/Entity Type

Hair And Beauty

Font styles to use
Serif

Colors
2f73b3
ffc214

Requirements
Must have
• Must use deep blue (royal blue) background and gold text (to align with brand name). Must use luxurious fonts
Nice to have
• Flowers or other natural symbols, pictures that blend well with the product theme

```html
<!DOCTYPE html>
<html lang="en">
<head>
<meta charset="utf-8">
<title>Velmora Hair Growth Oil — Packaging Panels</title>
<link href="https://fonts.googleapis.com/css2?family=Federo&family=Pathway+Gothic+One&display=swap" rel="stylesheet">
<style>
  :root {
    --backdrop: #ebebeb;
    --navy: #1c2548;
    --navy-light: #2a3560;
    --gold: #c9963f;
    --gold-soft: #a87a32;
    --panel-height: 760px;
  }
  * { box-sizing: border-box; margin: 0; padding: 0; }
  html, body {
    width: 1200px;
    height: 1200px;
    overflow: hidden;
    background: var(--backdrop);
  }
  .canvas {
    width: 1200px;
    height: 1200px;
    display: flex;
    align-items: center;
    justify-content: center;
    gap: 28px;
  }
  .panel {
    height: var(--panel-height);
    background: linear-gradient(180deg, var(--navy-light) 0%, var(--navy) 100%);
    color: var(--gold);
    display: flex;
    flex-direction: column;
    align-items: center;
    position: relative;
    overflow: hidden;
  }
  .panel--side-story { width: 262px; padding: 110px 22px 60px; }
  .panel--front { width: 300px; padding: 90px 24px 0; }
  .panel--side-claim { width: 220px; padding: 80px 20px 0; }
  .panel--label {
    width: 250px;
    height: 400px;
    padding: 46px 20px 30px;
    border-radius: 4px;
    justify-content: flex-start;
  }

  .wordmark {
    display: flex;
    align-items: center;
    gap: 8px;
    font-family: "Federo", sans-serif;
    color: var(--gold);
    letter-spacing: 0.08em;
    text-transform: uppercase;
  }
  .wordmark__dot {
    width: 9px;
    height: 9px;
    border-radius: 50%;
    background: var(--gold);
  }
  .panel--front .wordmark { font-size: 26px; margin-bottom: 40px; }
  .panel--label .wordmark { font-size: 20px; margin-bottom: 22px; }

  .product-title {
    font-family: "Pathway Gothic One", sans-serif;
    font-weight: 400;
    text-align: center;
    line-height: 1.15;
  }
  .panel--front .product-title { font-size: 56px; }
  .panel--label .product-title {
    font-family: "Federo", sans-serif;
    font-size: 32px;
    line-height: 1.2;
  }

  .base-note {
    font-family: "Pathway Gothic One", sans-serif;
    text-align: center;
    line-height: 1.3;
  }
  .panel--front .base-note { font-size: 26px; margin-top: 90px; }
  .panel--label .base-note {
    font-family: "Federo", sans-serif;
    font-size: 19px;
    margin-top: 20px;
  }

  .volume {
    font-family: "Pathway Gothic One", sans-serif;
  }
  .panel--side-story .volume { font-size: 44px; margin-top: auto; }
  .panel--label .volume {
    font-family: "Federo", sans-serif;
    font-size: 22px;
    margin-top: 28px;
  }

  .story-copy {
    font-family: "Pathway Gothic One", sans-serif;
    font-size: 24px;
    line-height: 1.36;
    text-align: center;
  }
  .herb-illustration {
    width: 190px;
    height: 260px;
    margin-top: 60px;
    background: radial-gradient(ellipse at 50% 60%, rgba(201,150,63,0.45) 0%, rgba(201,150,63,0.12) 60%, transparent 78%);
  }
  .coconut-illustration {
    position: absolute;
    left: 0;
    bottom: 0;
    width: 100%;
    height: 280px;
    background: radial-gradient(ellipse at 50% 85%, rgba(201,150,63,0.5) 0%, rgba(201,150,63,0.15) 55%, transparent 80%);
  }

  .follicle-illustration {
    width: 110px;
    height: 180px;
    margin-bottom: 70px;
    background: radial-gradient(ellipse at 50% 60%, rgba(201,150,63,0.4) 0%, rgba(201,150,63,0.1) 60%, transparent 80%);
  }
  .claim-copy {
    font-family: "Pathway Gothic One", sans-serif;
    font-size: 25px;
    line-height: 1.45;
    text-align: center;
  }
</style>
</head>
<body>
  <main class="canvas">

    <section class="panel panel--side-story">
      <p class="story-copy">Velmora Hair Growth Oil is a coconut oil based product that was developed by tribes in the Southern State of Kerala that includes ancient herbs like Gooseberry, Indigo, Indian Aloe, Balloon Vine, and Brahmi.</p>
      <div class="herb-illustration" role="img" aria-label="Gold line illustration of aloe leaves, gooseberries and herb sprigs"></div>
      <p class="volume">50ml</p>
    </section>

    <section class="panel panel--front">
      <div class="wordmark"><span class="wordmark__dot"></span>Velmora</div>
      <h1 class="product-title">Hair Growth<br>Oil</h1>
      <p class="base-note">Coconut Oil<br>Based</p>
      <div class="coconut-illustration" role="img" aria-label="Gold line illustration of coconuts among palm fronds"></div>
    </section>

    <section class="panel panel--side-claim">
      <div class="follicle-illustration" role="img" aria-label="Gold line illustration of a single hair growing from the scalp"></div>
      <p class="claim-copy">To help regrow hair.<br>Stronger, thicker,<br>and healthier hair.</p>
    </section>

    <section class="panel panel--label">
      <div class="wordmark"><span class="wordmark__dot"></span>Velmora</div>
      <h2 class="product-title">Hair Growth<br>Oil</h2>
      <p class="base-note">Coconut Oil<br>Based</p>
      <p class="volume">50ml</p>
    </section>

  </main>
</body>
</html>
```